Namecard Designs+Logo for a High End Automobile Company

We need a new business card for our company called Velta Motorhof.

www.veltamotorhof.example.sg
Our new website will be up in 2.5 months time.

We sell used and brand new continental cars like Korvane, QTL, Dravell, Solbrini and etc. Currently we are operating from 2 offices in Singapore and United Kingdom.

We want a design which is serious. We are open to colours but try to keep it at a maximum of 3 colours.

We prefer something simple and minimal. We are open to 2 sides printing or even 2 sided namecards. Both UK and Singapore company offices address must be in; either side by side, front and back, or even 2 sided cards.

The logo can be a text logo, emblem, abstract, pictorial or combination.

We are printing with Pribo.com so please kindly follow the printing guideline.

http://uk.pribo.example/help/faq/templates-and-guidelines.html

Rich and Car Enthusiasts

Printing

Must have
• Our 2 offices; UK and Singapore.

Our slogan which is " The Automobile Specialist"
Should not have
• Not more than 3 colours

```html
<!DOCTYPE html>
<html lang="en">
<head>
<meta charset="utf-8">
<title>Velta Motorhof – Business Card</title>
<link rel="stylesheet" href="https://fonts.googleapis.com/css2?family=Michroma&family=Roboto:wght@700;900&display=swap">
<style>
  :root {
    --page-bg: #ffffff;
    --card-black: #050505;
    --weave-dark: #111111;
    --weave-mid: #3a3a3a;
    --text-white: #ffffff;
    --caption: #222222;
    --band-light: #d9d9d9;
    --band-dark: #6a6a6a;
  }
  * { box-sizing: border-box; margin: 0; padding: 0; }
  html, body {
    width: 1200px;
    height: 902px;
    overflow: hidden;
    background: var(--page-bg);
  }
  .stage {
    position: relative;
    width: 1200px;
    height: 902px;
  }
  .card {
    position: absolute;
    top: 190px;
    height: 312px;
    width: 478px;
    background: var(--card-black);
    color: var(--text-white);
    overflow: hidden;
  }
  .card--front { left: 81px; }
  .card--back { left: 636px; }

  .card__texture {
    position: absolute;
    inset: 0;
    background: radial-gradient(ellipse at 50% 50%, var(--weave-mid) 0%, var(--weave-dark) 70%, #000 100%);
  }

  .brand {
    position: absolute;
    left: 0;
    right: 0;
    text-align: center;
  }
  .brand__name {
    font-family: "Michroma", sans-serif;
    font-size: 27px;
    line-height: 1;
    letter-spacing: 0.5px;
    color: var(--text-white);
    white-space: nowrap;
  }
  .brand__slogan {
    margin-top: 8px;
    font-family: "Roboto", sans-serif;
    font-weight: 900;
    font-size: 14px;
    letter-spacing: 1.5px;
    color: var(--text-white);
  }
  .card--front .brand { top: 127px; }
  .card--back .brand { top: 33px; }

  .office {
    position: absolute;
    left: 0;
    width: 100%;
    height: 66px;
  }
  .office--first { top: 120px; }
  .office--second { top: 204px; }
  .office__icon {
    position: absolute;
    left: 110px;
    top: 17px;
    width: 32px;
    height: 32px;
  }
  .office__address {
    position: absolute;
    left: 188px;
    width: 100px;
    top: 6px;
    text-align: center;
    font-family: "Roboto", sans-serif;
    font-weight: 700;
    font-size: 14px;
    line-height: 22px;
  }
  .office-divider {
    position: absolute;
    left: 24px;
    right: 24px;
    top: 191px;
    height: 2px;
    background: var(--text-white);
  }
  .card__band {
    position: absolute;
    left: 0;
    right: 0;
    bottom: 0;
    height: 28px;
    background: linear-gradient(to bottom, var(--band-dark), var(--band-light) 55%, #f4f4f4);
  }
  .caption {
    position: absolute;
    top: 684px;
    width: 200px;
    text-align: center;
    font-family: "Roboto", sans-serif;
    font-weight: 700;
    font-size: 21px;
    color: var(--caption);
  }
  .caption--front { left: 220px; }
  .caption--back { left: 775px; }
</style>
</head>
<body>
<main class="stage">
  <section class="card card--front" aria-label="Card front">
    <div class="card__texture" role="img" aria-label="Dark woven carbon-fibre texture"></div>
    <div class="brand">
      <div class="brand__name">VELTA MOTORHOF</div>
      <div class="brand__slogan">European Automobile Specialist</div>
    </div>
  </section>

  <section class="card card--back" aria-label="Card back">
    <div class="brand">
      <div class="brand__name">VELTA MOTORHOF</div>
      <div class="brand__slogan">European Automobile Specialist</div>
    </div>

    <div class="office office--first">
      <svg class="office__icon" viewBox="0 0 32 32" aria-hidden="true">
        <circle cx="16" cy="16" r="15" fill="#fff"/>
        <circle cx="16" cy="16" r="11" fill="none" stroke="#050505" stroke-width="2"/>
        <path d="M13 10 L19 16 L13 22" fill="none" stroke="#050505" stroke-width="3.2" stroke-linecap="round" stroke-linejoin="round"/>
      </svg>
      <div class="office__address">Street<br>Suburb<br>City</div>
    </div>

    <div class="office-divider"></div>

    <div class="office office--second">
      <svg class="office__icon" viewBox="0 0 32 32" aria-hidden="true">
        <circle cx="16" cy="16" r="15" fill="#fff"/>
        <circle cx="16" cy="16" r="11" fill="none" stroke="#050505" stroke-width="2"/>
        <path d="M13 10 L19 16 L13 22" fill="none" stroke="#050505" stroke-width="3.2" stroke-linecap="round" stroke-linejoin="round"/>
      </svg>
      <div class="office__address">Street<br>Suburb<br>City</div>
    </div>

    <div class="card__band"></div>
  </section>

  <p class="caption caption--front">Front</p>
  <p class="caption caption--back">Back</p>
</main>
</body>
</html>
```